Dova Lenthe Christmas Card 2025

I need a Christmas card design for Dova Lenthe (www.dovalenthe.example). My client loves everything Mara Quillon. I’ve attached this year’s inspirations, including the live wreath she is gifting and the brand guidelines. She prefers the softer colors shown in the inspiration materials. The greeting should read Merry Christmas (not Happy Holidays). The final design should feel elegant, festive, and aligned with the Dova Lenthe brand.”

```html
<!DOCTYPE html>
<html lang="en">
<head>
<meta charset="utf-8">
<title>Dova Lenthe Christmas Card 2025</title>
<link rel="stylesheet" href="https://fonts.googleapis.com/css2?family=Josefin+Sans:wght@300;400&display=swap">
<style>
  :root {
    --backdrop: #e6e4e1;
    --card-white: #ffffff;
    --blush: #f3e0dc;
    --blush-glow: #f7ebe8;
    --orange: #ef7d22;
    --pine: #5f8f4e;
    --pine-light: #a9c79b;
    --cocoa: #3b1a12;
  }
  * { margin: 0; padding: 0; box-sizing: border-box; }
  html, body { width: 1200px; height: 1200px; overflow: hidden; }
  body {
    background: var(--backdrop);
    font-family: "Josefin Sans", "Helvetica Neue", Arial, sans-serif;
    position: relative;
  }
  .card {
    position: absolute;
    left: 220px; top: 45px;
    width: 760px; height: 1110px;
    background: var(--card-white);
    padding: 28px;
  }
  .card__face {
    position: relative;
    width: 100%; height: 100%;
    background: radial-gradient(circle at 50% 30%, var(--blush-glow) 0%, var(--blush) 60%);
    overflow: hidden;
  }
  .wreath {
    position: absolute;
    left: 72px; top: 60px;
    width: 560px; height: 560px;
    border-radius: 50%;
    background: radial-gradient(circle, var(--pine) 0%, var(--pine) 48%, var(--pine-light) 62%, rgba(243,224,220,0) 72%);
  }
  .emblem {
    position: absolute;
    left: 202px; top: 190px;
    width: 300px; height: 300px;
    border-radius: 50%;
    background: var(--orange);
    display: flex; align-items: center; justify-content: center;
  }
  .emblem__name {
    color: var(--blush-glow);
    font-weight: 300;
    font-size: 34px;
    letter-spacing: 4px;
    text-transform: uppercase;
    text-align: center;
    line-height: 1.2;
  }
  .greeting {
    position: absolute;
    left: 120px; top: 640px;
    width: 560px;
  }
  .greeting__year {
    color: var(--card-white);
    font-weight: 400;
    font-size: 30px;
    letter-spacing: 14px;
  }
  .greeting__lead {
    margin-top: 10px;
    color: var(--cocoa);
    font-size: 12px;
    letter-spacing: 8px;
    text-transform: uppercase;
  }
  .greeting__merry {
    margin-top: 10px;
    color: var(--orange);
    font-weight: 300;
    font-size: 50px;
    letter-spacing: 2px;
    line-height: 1;
  }
  .greeting__christmas {
    margin-left: -8px;
    color: var(--orange);
    font-weight: 300;
    font-size: 94px;
    letter-spacing: 1px;
    line-height: 1;
  }
  .signature {
    position: absolute;
    left: 330px; top: 925px;
    color: var(--cocoa);
    font-weight: 400;
    font-size: 44px;
    letter-spacing: 3px;
    line-height: 1.05;
    text-transform: uppercase;
  }
</style>
</head>
<body>
  <div class="card">
    <div class="card__face">
      <div class="wreath" role="img" aria-label="Snow-dusted pine wreath with pinecones, red berries and bare twigs"></div>
      <div class="emblem">
        <span class="emblem__name">Dova<br>Lenthe</span>
      </div>
      <div class="greeting">
        <p class="greeting__year">2025</p>
        <p class="greeting__lead">Wishing you a happy</p>
        <p class="greeting__merry">MERRY</p>
        <p class="greeting__christmas">CHRISTMAS</p>
      </div>
      <p class="signature">Dova<br>Lenthe</p>
    </div>
  </div>
</body>
</html>
```